Young Accounting firm needing a captivating business card

We need a business card design that forces the person to look at the card because its either gold foil, plastic, or lettering pop up etc. We already have a logo with a specific gold color and we need to make it pop. We are an accounting firm. I need the words" accounting, payroll, licenses, audits, taxes" somewhere on the business card so as to describe what we do- preferably on the side where the logo is at.

Industry/Entity Type

Accounting

Contact Information for Business Card

Address 48276 9th Ave S Ste 305, Federal Way, WA 98117
Business Phone (360)418-2096
Fax (360)418-2157
Office Cell Phone (360)586-7319

Font styles to use
Serif

Colors
85abd2

Requirements
Must have
• It should state
• "Accounting" "Taxes" "Audits" "Licenses" "Payroll"
Nice to have
• Matte with gold foil, different textures, With Either a textured ivory background or gray blue slate background
Should not have
• colorful colors

```html
<!DOCTYPE html>
<html lang="en">
<head>
<meta charset="utf-8">
<title>Vantrel Ledger – Business Card</title>
<link rel="stylesheet" href="https://fonts.googleapis.com/css2?family=Poppins:wght@400;500&display=swap">
<style>
  :root {
    --backdrop: #222120;
    --card-white: #ffffff;
    --gold: #bb9916;
    --text-dark: #4a4a4a;
    --text-muted: #8d8d8d;
    --divider: #9a9a9a;
    --on-gold: #ffffff;
  }
  * { margin: 0; padding: 0; box-sizing: border-box; }
  html, body { width: 1125px; height: 1200px; overflow: hidden; }
  body {
    background: var(--backdrop);
    font-family: "Poppins", sans-serif;
    position: relative;
  }
  .card {
    position: absolute;
    left: 171px;
    width: 826px;
    height: 472px;
  }
  .card-front { top: 106px; background: var(--card-white); }
  .card-back { top: 639px; background: var(--gold); }

  .brand-name {
    position: absolute;
    left: 0;
    width: 100%;
    text-align: center;
    font-weight: 500;
    letter-spacing: -1px;
    white-space: nowrap;
  }
  .card-front .brand-name {
    left: 50px;
    width: 380px;
    top: 250px;
    font-size: 40px;
    color: var(--gold);
  }
  .card-back .brand-name {
    top: 230px;
    font-size: 48px;
    color: var(--on-gold);
  }

  .divider {
    position: absolute;
    left: 459px;
    top: 102px;
    width: 1px;
    height: 268px;
    background: var(--divider);
  }

  .contact-block {
    position: absolute;
    left: 492px;
    top: 98px;
    color: var(--text-dark);
  }
  .person-name {
    font-size: 30px;
    font-weight: 500;
    color: var(--gold);
    line-height: 1.1;
  }
  .person-title {
    font-size: 17px;
    font-weight: 500;
    color: var(--text-muted);
    line-height: 1.2;
  }
  .address {
    margin-top: 15px;
    font-size: 18px;
    line-height: 23px;
  }
  .contact-list {
    list-style: none;
    margin-top: 16px;
  }
  .contact-list li {
    display: flex;
    align-items: center;
    font-size: 18.5px;
    line-height: 27.5px;
  }
  .contact-list svg {
    width: 18px;
    height: 18px;
    margin-right: 13px;
    fill: var(--gold);
    flex: none;
  }

  .services {
    position: absolute;
    left: 0;
    width: 100%;
    top: 402px;
    text-align: center;
    font-size: 19px;
    color: var(--on-gold);
  }
</style>
</head>
<body>
  <section class="card card-front">
    <div class="brand-name">Vantrel Ledger</div>
    <div class="divider"></div>
    <div class="contact-block">
      <div class="person-name">Daniel Morrow</div>
      <div class="person-title">Founder &amp; CEO</div>
      <p class="address">48276 9th Ave S Ste 305,<br>Federal Way, WA 98117</p>
      <ul class="contact-list">
        <li>
          <svg viewBox="0 0 24 24" aria-hidden="true"><path d="M6.6 10.8a15.1 15.1 0 0 0 6.6 6.6l2.2-2.2c.3-.3.7-.4 1-.2 1.1.4 2.3.6 3.6.6.6 0 1 .4 1 1V20c0 .6-.4 1-1 1A17 17 0 0 1 3 4c0-.6.4-1 1-1h3.5c.6 0 1 .4 1 1 0 1.3.2 2.5.6 3.6.1.3 0 .7-.2 1z"/></svg>
          (360)418-2096
        </li>
        <li>
          <svg viewBox="0 0 24 24" aria-hidden="true"><path d="M7 1h10a2 2 0 0 1 2 2v18a2 2 0 0 1-2 2H7a2 2 0 0 1-2-2V3a2 2 0 0 1 2-2zm0 3v14h10V4zm5 15.5a1 1 0 1 0 0 2 1 1 0 0 0 0-2z"/></svg>
          (360)586-7319
        </li>
        <li>
          <svg viewBox="0 0 24 24" aria-hidden="true"><path d="M6 2h9l3 3v5H6zM3 11h18a1 1 0 0 1 1 1v7H2v-7a1 1 0 0 1 1-1zm3 4v2h12v-2zM2 20h20v2H2z"/></svg>
          (360)418-2157
        </li>
        <li>
          <svg viewBox="0 0 24 24" aria-hidden="true"><path d="M2 5h20v14H2zm2 2v.5l8 5 8-5V7l-8 5z"/></svg>
          info@vantrelledger.com
        </li>
        <li>
          <svg viewBox="0 0 24 24" aria-hidden="true"><path d="M12 2a10 10 0 1 0 0 20 10 10 0 0 0 0-20zm-1 17.9A8 8 0 0 1 4.2 10.2L9 15v1a2 2 0 0 0 2 2zm6.9-2.5A2 2 0 0 0 16 16h-1v-3a1 1 0 0 0-1-1H8v-2h2a1 1 0 0 0 1-1V7h2a2 2 0 0 0 2-2v-.4a8 8 0 0 1 2.9 12.8z"/></svg>
          www.vantrelledger.com
        </li>
      </ul>
    </div>
  </section>

  <section class="card card-back">
    <div class="brand-name">Vantrel Ledger</div>
    <p class="services">Accounting • Taxes • Audits • Licenses • Payroll</p>
  </section>
</body>
</html>
```